Corporate Identity Design Project

Teslin Varrow Design is a small boutique event planning and floral design company, based in Northern Alberta. I require the creation of some corporate identity pieces. I want a minimalistic design.
Website www.teslinvarrow.example

Pieces should include
1. Business Card
Should include the company logo, name, email address, address, phone number. These will be professional printed.
These are three cards that I like:
http://cardsamplegallery.example/wp-content/uploads/2010/02/Odile_Vantreck_Roomworks_by_Pepperleaf_studio_Media.jpg
http://neatcardshowcase.example/wp-content/uploads/2011/06/Quiet-Studio-Minimalist-Business-Cards_11.jpg
http://graphicfeedhub.example/wp-content/uploads/2012/03/16.minimalist-business-cards.jpg
I like letterpress, but I am open to other options.

2. Letterhead
will be professionally printed

3. Envelope

4. Fax Sheet
will be printed on home printer

5. Pocket Presentation
Like -http://wrenfieldgardens.example/img/design_step_proposal@2x.jpg

6. Invoice
Like - http://samplehost.example/quillmarsh/2011/02/falcon-athletics-4-letterhead-combined.png?w=529

7. Proposal
Like something like this – this will not be printed, but rather emailed to clients
Like http://files7.imagedepot.example/getfile/files.imagedepot.example/trelvo-studio/nkuBfi2LVj7ENiUb5D16wqAHQHqNNT5vut7mukSTmisfoGHYXGEv9haEQOPL/Picture-52.png.scaled.500.jpg

8. Contract
Like http://www.brightkeyadvertising.example/images/sample-contract.jpg

9. Business Brochure – I have removed this piece from the project and will most likely post it as another project at a later date.

If you think that this is a project of interest to you, but feel that it is “too much” work for the price, please let me know how you would re-package it – I am open to suggestions.

Target Market(s)

Young women

Industry/Entity Type

Boutique

Requirements
Should not have
• I do not want it to look "frilly"

```html
<!DOCTYPE html>
<html lang="en">
<head>
<meta charset="utf-8">
<title>Teslin Varrow Design — Business Card</title>
<link rel="stylesheet" href="https://fonts.googleapis.com/css2?family=Jost:wght@400;500;600&display=swap">
<style>
  :root {
    --page-bg: #d8d4cf;
    --card-bg: #eef0f1;
    --ink: #3e3e3b;
    --mauve: #a0636b;
    --card-shadow: rgba(40, 30, 20, 0.18);
  }
  * { margin: 0; padding: 0; box-sizing: border-box; }
  html, body {
    width: 1200px;
    height: 880px;
    overflow: hidden;
  }
  body {
    background: var(--page-bg);
    font-family: "Jost", "Futura", sans-serif;
    color: var(--ink);
    display: flex;
    align-items: center;
    justify-content: center;
    gap: 44px;
  }
  .card {
    position: relative;
    width: 530px;
    height: 303px;
    background: var(--card-bg);
    box-shadow: 0 6px 18px var(--card-shadow);
  }

  /* Front */
  .card-front {
    display: flex;
    align-items: center;
    padding-left: 62px;
  }
  .brand {
    display: flex;
    align-items: center;
    gap: 26px;
  }
  .brand-dot {
    width: 96px;
    height: 96px;
  }
  .brand-name {
    font-weight: 600;
    font-size: 30px;
    line-height: 1.04;
    letter-spacing: 0.14em;
    text-transform: uppercase;
    color: var(--ink);
  }

  /* Back */
  .card-back {
    text-transform: uppercase;
  }
  .contact-line {
    position: absolute;
    top: 22px;
    left: 26px;
    right: 26px;
    font-size: 13px;
    font-weight: 400;
    letter-spacing: 0.16em;
  }
  .contact-sep {
    margin: 0 6px;
  }
  .holder-name {
    position: absolute;
    top: 118px;
    left: 0;
    right: 0;
    text-align: center;
    font-weight: 600;
    font-size: 28px;
    line-height: 1.02;
    letter-spacing: 0.16em;
  }
  .address-line {
    position: absolute;
    bottom: 22px;
    left: 26px;
    right: 26px;
    font-size: 13px;
    letter-spacing: 0.16em;
  }
</style>
</head>
<body>
  <section class="card card-front" aria-label="Business card, front">
    <div class="brand">
      <svg class="brand-dot" viewBox="0 0 96 96" aria-hidden="true">
        <circle cx="48" cy="48" r="40" fill="var(--mauve)"/>
      </svg>
      <p class="brand-name">Teslin<br>Varrow<br>Design</p>
    </div>
  </section>

  <section class="card card-back" aria-label="Business card, back">
    <p class="contact-line">name.surname@domain.com<span class="contact-sep">•</span>(+00) 123 456 789</p>
    <h1 class="holder-name">Teslin<br>Varrow</h1>
    <p class="address-line">Your address goes here, city, country, zipcode</p>
  </section>
</body>
</html>
```